Help Liu Wenhao redesign his business card!

Liu Wenhao, an "influential" Chinese businessman, made international headlines this week with his business card...but not for the right reasons. Help Liu Wenhao redesign his new business card - funny and/or satirical submissions welcome!

Check out his hilarious business card that he was giving out on a trip to New York, with not one, not two...but TEN titles! Let's just say they're not the most humble titles either :).

Read more about Liu's business card here: http://blogs.brightledger.example/asiadesk/2014/01/14/liu-wenhaos-business-card-needs-to-be-recycled/

While the rest of the world is laughing at him, we want to help. This is an unofficial contest, but we'd like the PixelForge community to have a shot at redesigning Liu's business card. Thousands of businesses have used PixelForge.example to create beautiful business cards, so we know the community of designers here can do a great job.

We'd like you to create a business card worthy of this honorable businessman, while also keeping a clean, dignified design.

Funny / satirical job titles and designs are encouraged. Note you do not have to use all of Liu's titles on the card. Feel free to come up with your own creative titles!

In regard to contact details, please use dummy contact details. Liu's company name and street address are:

China Tai-Mo Reusable Scrap & Restoration Corporation
Fuxing Road 7, Lanqiao District, Nanjing, China

You can design a single sided or double-sided card - it's completely up to you!

Target Market(s)

Business people and government officials of the world

Industry/Entity Type

Business

Font styles to use
Serif
Sans Serif
Decorative

Colors
ec2027
ffc214
6b449b
0455a3

Requirements
Must have
• At least 1 title, preferably more than 1.

Designers can approach this task how they like however one option could be to use one of Liu's titles and create a suitable business card graphic to suit the role. Designers are also encouraged to o make up a new title and design a graphic to suit.

Here are the titles - but you can also make up your own!

Foremost Card-Recycling Expert
Most prominent Philanthropist of China
Humble Title Collector
China Earthquake Rescue Hero
Most well-known and Beloved Chinese Role Model
China Top Ten Most Honorable Volunteer
Most Charismatic Philanthropist of China
China Low Carbon Emission
Environmental Protection Top Advocate
China's Foremost Environmental Preservation Demolition Expert
Should not have
• No black borders around photographs of Liu Wenhao
Do not present Liu Wenhao's image in grayscale (black and white)

For a detailed guideline for colors to avoid in design targeting the Chinese market, see http://www.corvalegroup.example/2011/01/17/color/

```html
<!DOCTYPE html>
<html lang="en">
<head>
<meta charset="utf-8">
<title>Wenhao Liu – Business Card Colourways</title>
<link rel="stylesheet" href="https://fonts.googleapis.com/css2?family=Arimo:wght@400;700&display=swap">
<style>
  :root {
    --page-bg: #ffffff;
    --card-bg: #cdcccc;
    --blue: #0455a3;
    --purple: #6b449b;
    --red: #ec2027;
    --white: #ffffff;
  }
  * { box-sizing: border-box; margin: 0; padding: 0; }
  html, body { width: 1200px; height: 1000px; overflow: hidden; background: var(--page-bg); }
  body { position: relative; font-family: "Arimo", Arial, sans-serif; }

  .hero-portrait {
    position: absolute; left: 500px; top: 65px; width: 252px; height: 302px;
    background: linear-gradient(180deg, #ffffff 0%, #d7e3f1 45%, var(--blue) 100%);
  }

  .card {
    position: absolute; top: 737px; width: 345px; height: 189px;
    background: var(--card-bg); color: var(--accent); overflow: hidden;
  }
  .card--blue   { left: 78px;  --accent: var(--blue); }
  .card--purple { left: 432px; --accent: var(--purple); }
  .card--red    { left: 785px; --accent: var(--red); }

  .card__edge { position: absolute; left: 0; top: 0; width: 10px; height: 140px; background: var(--accent); }

  .card__portrait {
    position: absolute; left: 26px; top: 14px; width: 82px; height: 96px;
    background: linear-gradient(180deg, var(--card-bg) 0%, var(--accent) 100%);
  }
  .card__name {
    position: absolute; left: 16px; top: 114px; width: 104px; text-align: center;
    font-size: 9.5px; font-weight: 700; line-height: 12px; letter-spacing: 0.2px;
  }
  .card__role { display: block; font-weight: 400; letter-spacing: 2px; }

  .card__titles {
    position: absolute; right: 18px; top: 14px; text-align: right;
    font-size: 10px; font-weight: 700; line-height: 14px;
  }
  .card__titles li { list-style: none; }
  .card__titles li + li { margin-right: 20px; }

  .card__company {
    position: absolute; right: 14px; top: 82px; text-align: right;
    font-size: 13px; font-weight: 700; line-height: 17px;
  }

  .card__contact {
    position: absolute; left: 0; right: 0; bottom: 0; height: 50px;
    background: var(--accent); color: var(--white);
    font-size: 8.6px; line-height: 13px; padding: 8px 0 0 0; text-align: center;
    white-space: nowrap;
  }
  .card__contact .label { display: inline-block; width: 48px; text-align: left; }
</style>
</head>
<body>

  <div class="hero-portrait" role="img" aria-label="Illustrated portrait of Wenhao Liu in suit and tie, blue on white"></div>

  <article class="card card--blue">
    <div class="card__edge"></div>
    <div class="card__portrait" role="img" aria-label="Blue portrait illustration of Wenhao Liu"></div>
    <p class="card__name">WENHAO LIU<span class="card__role">CEO</span></p>
    <ul class="card__titles"><li>FOREMOST CARD-RECYCLING EXPERT</li><li>HUMBLE TITLE COLLECTOR</li></ul>
    <p class="card__company">China Tai-Mo<br>Reusable Scrap<br>&amp; Restoration Corporation</p>
    <div class="card__contact">
      <span class="label">Address:</span>Fuxing Road 7, Lanqiao District, Nanjing, China<br>
      Postal Code: 098765&nbsp; Tel: (02)-9876-54321098 Fax: (02)-9876-54321097<br>
      Mobile: 09876543210&nbsp; E-mail: wenhao@liu.example
    </div>
  </article>

  <article class="card card--purple">
    <div class="card__edge"></div>
    <div class="card__portrait" role="img" aria-label="Purple portrait illustration of Wenhao Liu"></div>
    <p class="card__name">WENHAO LIU<span class="card__role">CEO</span></p>
    <ul class="card__titles"><li>FOREMOST CARD-RECYCLING EXPERT</li><li>HUMBLE TITLE COLLECTOR</li></ul>
    <p class="card__company">China Tai-Mo<br>Reusable Scrap<br>&amp; Restoration Corporation</p>
    <div class="card__contact">
      <span class="label">Address:</span>Fuxing Road 7, Lanqiao District, Nanjing, China<br>
      Postal Code: 098765&nbsp; Tel: (02)-9876-54321098 Fax: (02)-9876-54321097<br>
      Mobile: 09876543210&nbsp; E-mail: wenhao@liu.example
    </div>
  </article>

  <article class="card card--red">
    <div class="card__edge"></div>
    <div class="card__portrait" role="img" aria-label="Red portrait illustration of Wenhao Liu"></div>
    <p class="card__name">WENHAO LIU<span class="card__role">CEO</span></p>
    <ul class="card__titles"><li>FOREMOST CARD-RECYCLING EXPERT</li><li>HUMBLE TITLE COLLECTOR</li></ul>
    <p class="card__company">China Tai-Mo<br>Reusable Scrap<br>&amp; Restoration Corporation</p>
    <div class="card__contact">
      <span class="label">Address:</span>Fuxing Road 7, Lanqiao District, Nanjing, China<br>
      Postal Code: 098765&nbsp; Tel: (02)-9876-54321098 Fax: (02)-9876-54321097<br>
      Mobile: 09876543210&nbsp; E-mail: wenhao@liu.example
    </div>
  </article>

</body>
</html>
```